Brevin Finance Flyer Design

I would like a high res flyer designed for mass printing. It is for a mortgage and finance broking company in Sydney. We are called Brevin Finance. The wording i would like displayed is the following
Looking For Something Extra from your broker?
Brevin Finance can make all the difference
What we offer you is an extensive range of mortgage and finance products, including:
• Home Loans
• Investment Loans
• Low Doc Loans
• Vehicle Finance
• Equipment Finance
• Commercial Loans
• Refinance
Contact Us
Phone (02) 7354 2816
email info@brevinfinance.com.au
web www.brevinfinance.com.au
Finance

```html
<!DOCTYPE html>
<html lang="en">
<head>
<meta charset="utf-8">
<title>Brevin Finance Flyer</title>
<link rel="stylesheet" href="https://fonts.googleapis.com/css2?family=Arimo:wght@400;700&display=swap">
<style>
  :root {
    --page-bg: #ffffff;
    --flyer-bg: #ffffff;
    --brand-blue: #5ea7dc;
    --heading-blue: #5aa3d9;
    --logo-grey: #4d4d4f;
    --text-dark: #222222;
    --rule-black: #111111;
    --photo-light: #eef4f9;
    --photo-mid: #c6d6e5;
    --photo-dark: #26395f;
  }
  * { box-sizing: border-box; margin: 0; padding: 0; }
  html, body {
    width: 1200px; height: 1000px; overflow: hidden;
    background: var(--page-bg);
    font-family: "Arimo", Arial, sans-serif;
  }
  .flyer {
    position: absolute; left: 303px; top: 60px;
    width: 594px; height: 842px;
    background: var(--flyer-bg);
    border: 1px solid #e2e2e2;
  }
  .brand {
    position: absolute; top: 30px; left: 0; width: 100%;
    display: flex; flex-direction: column; align-items: center;
  }
  .brand-name {
    display: flex; align-items: center; gap: 10px;
    font-size: 28px; font-weight: 400; color: var(--logo-grey); line-height: 1;
  }
  .brand-square { width: 22px; height: 22px; background: var(--logo-grey); }
  .brand-tagline {
    margin-top: 3px; margin-left: 32px;
    font-size: 9px; color: var(--logo-grey);
  }
  .headline-band {
    position: absolute; top: 100px; left: 0; width: 100%; height: 100px;
    background: var(--brand-blue);
    display: flex; flex-direction: column; justify-content: center; align-items: center;
    color: #fff; font-weight: 700; font-size: 19px; line-height: 25px; text-align: center;
  }
  .hero-photo {
    position: absolute; top: 200px; left: 0; width: 100%; height: 340px;
    background: linear-gradient(90deg, var(--photo-mid) 0%, var(--photo-light) 30%, #dfe8f1 48%, #b8c9dc 57%, var(--photo-dark) 66%, #1f3259 82%, var(--photo-mid) 95%);
  }
  .hero-rule {
    position: absolute; top: 540px; left: 0; width: 100%; height: 7px;
    background: var(--rule-black);
  }
  .offer-heading {
    position: absolute; top: 578px; left: 0; width: 100%;
    text-align: center; color: var(--heading-blue);
    font-weight: 700; font-size: 17.5px; line-height: 25px;
  }
  .product-list {
    position: absolute; top: 641px; left: 0; width: 100%;
    text-align: center; font-size: 14.5px; line-height: 20px; color: var(--text-dark);
  }
  .product-list li { display: inline; list-style: none; }
  .product-list li::before {
    content: ""; display: inline-block; width: 6px; height: 6px; border-radius: 50%;
    background: var(--heading-blue); margin: 0 8px 2px 6px; vertical-align: middle;
  }
  .contact {
    position: absolute; top: 730px; left: 40px;
  }
  .contact-title {
    font-size: 18px; font-weight: 700; color: var(--heading-blue); margin-bottom: 8px;
  }
  .contact-line { font-size: 14.5px; line-height: 20px; color: var(--text-dark); }
  .web-address {
    position: absolute; top: 776px; right: 40px;
    font-size: 18px; font-weight: 700; color: var(--heading-blue);
  }
</style>
</head>
<body>
  <main class="flyer">
    <header class="brand">
      <div class="brand-name"><span class="brand-square"></span>Brevin Finance</div>
      <div class="brand-tagline">mortgage and finance broking services</div>
    </header>

    <section class="headline-band">
      <p>Looking For Something Extra from your broker?</p>
      <p>Brevin Finance can make all the difference</p>
    </section>

    <div class="hero-photo" role="img" aria-label="Blurred business people walking through a bright office corridor"></div>
    <div class="hero-rule"></div>

    <h2 class="offer-heading">What we offer you is an extensive range of<br>mortgage and finance products, including:</h2>

    <ul class="product-list">
      <li>Home Loans</li>
      <li>Investment Loans</li>
      <li>Low Doc Loans</li>
      <li>Vehicle Finance</li><br>
      <li>Equipment Finance</li>
      <li>Commercial Loans</li>
      <li>Refinance</li>
    </ul>

    <section class="contact">
      <h3 class="contact-title">Contact Us</h3>
      <p class="contact-line">Phone: (02) 7354 2816</p>
      <p class="contact-line">Email: info@brevinfinance.com.au</p>
    </section>

    <p class="web-address">www.brevinfinance.com.au</p>
  </main>
</body>
</html>
```